ALL TEXT Social Media Graphics

We are looking for a series of social media graphics for Instagram (new size: 4:5 (1080 x 1350 pixels) ratio that are ALL TEXT. We want the following quotes below on each graphic; one quote per graphic. AND, In very small letters at the bottom of each graphic, add @KPBrandellLive
The look and feel of these graphics should be complimentary to the color palette attached below; but keep them simple. But the design is up to you; at the end of this document, I provided various samples of all text graphics that I like as examples.
The Quotes are in the attached WORD document
Target Market(s)
women trying to lose weight
Look and feel
Each slider illustrates characteristics of the customer's brand and the style your logo design should communicate.

```html
<!DOCTYPE html>
<html lang="en">
<head>
<meta charset="utf-8">
<title>Sun Girl Summer Shapeup</title>
<link rel="stylesheet" href="https://fonts.googleapis.com/css2?family=League+Gothic&family=Poppins:wght@700&family=Courier+Prime&display=swap">
<style>
  :root {
    --bg: #ffffff;
    --headline-pink: #ef6190;
    --band-magenta: #e4479a;
    --band-text: #fce8f1;
    --cta-berry: #b0145a;
  }
  * { margin: 0; padding: 0; box-sizing: border-box; }
  html, body {
    width: 960px;
    height: 1200px;
    overflow: hidden;
    background: var(--bg);
  }
  .post {
    position: relative;
    width: 960px;
    height: 1200px;
    background: var(--bg);
  }
  .headline {
    position: absolute;
    left: 44px;
    top: 58px;
    width: 880px;
    font-family: "League Gothic", "Oswald", sans-serif;
    font-weight: 400;
    font-size: 142px;
    line-height: 111px;
    color: var(--headline-pink);
    text-transform: uppercase;
    letter-spacing: 0.5px;
  }
  .offer-band {
    position: absolute;
    left: 44px;
    top: 537px;
    width: 876px;
    height: 320px;
    background: var(--band-magenta);
  }
  .offer-text {
    position: absolute;
    left: 29px;
    top: 18px;
    font-family: "League Gothic", "Oswald", sans-serif;
    font-weight: 400;
    font-size: 106px;
    line-height: 93px;
    color: var(--band-text);
    text-transform: uppercase;
    letter-spacing: 0.5px;
  }
  .cta {
    position: absolute;
    left: 44px;
    top: 893px;
    font-family: "Poppins", sans-serif;
    font-weight: 700;
    font-size: 71px;
    line-height: 85px;
    color: var(--cta-berry);
    text-transform: uppercase;
    letter-spacing: -0.5px;
  }
  .handle {
    position: absolute;
    left: 50px;
    top: 1108px;
    font-family: "Courier Prime", monospace;
    font-size: 34px;
    line-height: 40px;
    color: var(--cta-berry);
  }
</style>
</head>
<body>
  <main class="post">
    <h1 class="headline">This summer ain’t<br>over—and neither<br>are your body<br>goals.</h1>
    <section class="offer-band">
      <p class="offer-text">Drop 30 pounds<br>with the sun girl<br>summer shapeup.</p>
    </section>
    <p class="cta">Comment “Sun Girl”<br>to get the plan</p>
    <p class="handle">@KPBrandellLive</p>
  </main>
</body>
</html>
```